Personal development products that change your life

This is a direct selling business that sells personal development courses, but also sells the business as well if desired. This is not MLM, and there is no handling of the product required, nor hassling friends or family. We are looking for business minded people wanting to work their own hours and achieve a desirable income from this. A success image or happy image on a flyer would be great. I'd like the website address to be displayed as well thanks. www.gainpath-hub.com.au

Target Market(s)

Business-minded individuals searching for more finances. Self motivated, driven, interested in self development.

Industry/Entity Type

Business

Font styles to use
Sans Serif

Requirements
Must have
• Are you looking for
• - a franchise or business?
• - a change of career?
• - a back up income?
• Not MLM
• No product handling or shipping
• No hard sales required
• website: www.gainpath-hub.com.au
Nice to have
• A picture or background of excited person jumping in the air, or some similar.
• Worded to enrol people interested in achieving more financial headway, or flexible hours, or travel and do this business from anywhere in the world.
• Only need access to a phone, internet connection and a desire to succeed.

```html
<!DOCTYPE html>
<html lang="en">
<head>
<meta charset="utf-8">
<title>Are You Looking For? – GainPath Hub Flyer</title>
<link href="https://fonts.googleapis.com/css2?family=Bebas+Neue&family=Questrial&family=Montserrat:wght@600&display=swap" rel="stylesheet">
<style>
  :root {
    --page-bg: #e9eaec;
    --paper: #ffffff;
    --brand-dark: #1b67a6;
    --brand-light: #2c8bd6;
    --photo-light: #f4f8fc;
    --photo-mid: #a9cbea;
    --photo-deep: #6f9fcf;
    --text-light: #ffffff;
  }
  * { box-sizing: border-box; margin: 0; padding: 0; }
  html, body { width: 1092px; height: 1200px; overflow: hidden; }
  body { background: var(--page-bg); position: relative; }

  .flyer {
    position: absolute;
    left: 155px; top: 36px;
    width: 782px; height: 1130px;
    background: var(--paper);
    overflow: hidden;
  }
  .hero-photo {
    position: absolute;
    left: 0; top: 0; width: 782px; height: 560px;
    background:
      radial-gradient(ellipse 300px 300px at 400px 300px, var(--photo-mid) 0%, var(--photo-deep) 45%, rgba(169,203,234,0.35) 75%, transparent 100%),
      var(--photo-light);
  }
  .wave { position: absolute; left: 0; top: 0; width: 782px; height: 1130px; }

  .headline {
    position: absolute;
    left: 32px; top: 532px;
    font-family: "Bebas Neue", sans-serif;
    font-weight: 400;
    color: var(--text-light);
    font-size: 106px;
    line-height: 106px;
    letter-spacing: 9px;
  }
  .headline .line-two { display: block; padding-left: 98px; }

  .benefits {
    position: absolute;
    left: 25px; top: 768px;
    width: 352px;
    list-style: none;
    font-family: "Questrial", sans-serif;
    font-size: 22px;
    line-height: 27px;
    color: var(--text-light);
  }
  .benefits li { position: relative; padding-left: 24px; }
  .benefits li::before {
    content: "";
    position: absolute; left: 0; top: 7px;
    width: 14px; height: 14px;
    background: var(--text-light);
  }
  .column-rule {
    position: absolute;
    left: 384px; top: 762px;
    width: 6px; height: 266px;
    background: var(--text-light);
  }
  .pitch {
    position: absolute;
    left: 404px; top: 778px;
    width: 354px;
    font-family: "Questrial", sans-serif;
    font-size: 22px;
    line-height: 27px;
    color: var(--text-light);
    text-align: justify;
    letter-spacing: 0.2px;
  }
  .pitch p + p { margin-top: 13px; }

  .footer-band {
    position: absolute;
    left: 0; top: 1068px;
    width: 782px; height: 48px;
    background: var(--paper);
    display: flex; align-items: center; justify-content: center;
    font-family: "Montserrat", sans-serif;
    font-weight: 600;
    font-size: 23px;
    color: var(--brand-dark);
    letter-spacing: 0.5px;
  }
  .footer-strip {
    position: absolute;
    left: 0; top: 1116px;
    width: 782px; height: 14px;
    background: var(--brand-dark);
  }
</style>
</head>
<body>
  <main class="flyer">
    <div class="hero-photo" role="img" aria-label="Photo of an excited businessman in a blue shirt and tie cheering with both fists raised behind a laptop"></div>

    <svg class="wave" viewBox="0 0 782 1130" aria-hidden="true">
      <path d="M0 297 C 200 390, 450 480, 782 519 L782 1130 L0 1130 Z" fill="var(--brand-light)"/>
      <path d="M0 356 C 220 440, 470 540, 782 570 L782 1130 L0 1130 Z" fill="var(--brand-dark)"/>
    </svg>

    <h1 class="headline">Are you<span class="line-two">looking for?</span></h1>

    <ul class="benefits">
      <li>Franchise or a business to work</li>
      <li>Change of career</li>
      <li>Business that suits all abilities - and some disabilities</li>
      <li>Extra cash, extra time, flexible hours, flexible location</li>
      <li>Create your own financial security</li>
      <li>Not MLM</li>
    </ul>

    <div class="column-rule"></div>

    <div class="pitch">
      <p>Enrol people interested in achieving more financial headway, or flexible hours, or travel and do this business from anywhere in the world.</p>
      <p>Only need access to a phone, internet connection and a desire to succeed.</p>
    </div>

    <div class="footer-band">Visit us at http://www.gainpath-hub.com.au/</div>
    <div class="footer-strip"></div>
  </main>
</body>
</html>
```